Direct to Consumer extended service contract business with a new disruptive business model needs a

We need a customized wordpress design for a company called 'Bright Harbor Assurance'.
We provide an innovative and unique service contract protection program direct to consumers. This program provides monthly coverage for all electronics purchased in the last 4 years and all electronics the consumer purchases in the future for a low monthly fee. The overall design should communicate a sense of legitimacy, ethics, and superior customer service and support (in an industry that has a huge PR issue to overcome).
Electronics is the first product group, other product groups with different price points to launch in the future..

Target Market(s)

All purchasers of electronic goods...all demographics

Industry/Entity Type

Electronics

Font styles to use
Sans Serif

Requirements
Must have
• Customer Testimonials
Industry News
Customer ratings
Blog posts
Call to action messaging
Like the functional elements and design of veltomarket.example (need to be better)
Nice to have
• Like to see video testimonials
Social network "whats trending related to electronics or service contract industry"
Easy way to register products for warranty

```html
<!DOCTYPE html>
<html lang="en">
<head>
<meta charset="utf-8">
<title>How do you get all of your products protected?</title>
<link rel="stylesheet" href="https://fonts.googleapis.com/css2?family=Montserrat:wght@700;800&display=swap">
<style>
  :root {
    --bg: #16191c;
    --accent: #f24f42;
    --icon: #a3a3a3;
    --text: #ffffff;
  }
  html, body {
    margin: 0;
    padding: 0;
    overflow: hidden;
    background: var(--bg);
  }
  .steps-section {
    position: relative;
    width: 1200px;
    height: 437px;
    background: var(--bg);
    overflow: hidden;
    font-family: "Montserrat", sans-serif;
  }
  .steps-title {
    position: absolute;
    top: 44px;
    left: 0;
    width: 100%;
    margin: 0;
    text-align: center;
    color: var(--text);
    font-weight: 800;
    font-size: 26px;
    letter-spacing: -0.2px;
  }
  .steps-graph {
    position: absolute;
    inset: 0;
  }
  .connector { stroke: var(--accent); stroke-width: 2; fill: none; }
  .node { fill: var(--accent); }
  .icon { fill: none; stroke: var(--icon); stroke-width: 2.4; stroke-linecap: round; stroke-linejoin: round; }
  .icon-fill { fill: var(--icon); }
  .step-label {
    fill: var(--text);
    font-family: "Montserrat", sans-serif;
    font-weight: 800;
    font-size: 10.5px;
    text-anchor: middle;
  }
</style>
</head>
<body>
<section class="steps-section">
  <h2 class="steps-title">HOW DO YOU GET ALL OF YOUR PRODUCTS PROTECTED?</h2>

  <svg class="steps-graph" width="1200" height="437" viewBox="0 0 1200 437" aria-hidden="false">
    <!-- title divider -->
    <g class="title-divider">
      <line class="connector" x1="461" y1="91" x2="516" y2="91"/>
      <line class="connector" x1="549" y1="91" x2="650" y2="91"/>
      <line class="connector" x1="683" y1="91" x2="735" y2="91"/>
      <g stroke="var(--accent)" stroke-width="3">
        <line x1="522" y1="97" x2="526" y2="85"/>
        <line x1="529" y1="97" x2="533" y2="85"/>
        <line x1="536" y1="97" x2="540" y2="85"/>
        <line x1="543" y1="97" x2="547" y2="85"/>
        <line x1="655" y1="85" x2="659" y2="97"/>
        <line x1="662" y1="85" x2="666" y2="97"/>
        <line x1="669" y1="85" x2="673" y2="97"/>
        <line x1="676" y1="85" x2="680" y2="97"/>
      </g>
    </g>

    <!-- connectors -->
    <g class="connectors">
      <line class="connector" x1="84" y1="252" x2="317" y2="194"/>
      <line class="connector" x1="317" y1="194" x2="569" y2="246"/>
      <line class="connector" x1="569" y1="246" x2="839" y2="147"/>
      <line class="connector" x1="839" y1="147" x2="1103" y2="261"/>
      <line class="connector" x1="84" y1="252" x2="211" y2="338"/>
      <line class="connector" x1="569" y1="246" x2="635" y2="138"/>
      <line class="connector" x1="1103" y1="261" x2="928" y2="293"/>
    </g>

    <!-- small dots -->
    <circle class="node" cx="211" cy="338" r="13"/>
    <circle class="node" cx="635" cy="138" r="13"/>
    <circle class="node" cx="928" cy="293" r="13"/>

    <!-- step 1: join membership network -->
    <g class="step step-join">
      <circle class="node" cx="84" cy="252" r="53"/>
      <g class="icon">
        <circle cx="84" cy="252" r="24"/>
        <ellipse cx="84" cy="252" rx="10" ry="24"/>
        <line x1="60" y1="252" x2="108" y2="252"/>
        <path d="M64 240 Q84 246 104 240"/>
        <path d="M64 264 Q84 258 104 264"/>
      </g>
      <text class="step-label" x="84" y="320">JOIN MEMBERSHIP</text>
      <text class="step-label" x="84" y="333">NETWORK</text>
    </g>

    <!-- step 2: select plan -->
    <g class="step step-plan">
      <circle class="node" cx="317" cy="194" r="45"/>
      <g class="icon">
        <rect x="300" y="176" width="14" height="26" rx="2" transform="rotate(-12 307 189)"/>
        <rect x="320" y="176" width="14" height="26" rx="2" transform="rotate(12 327 189)"/>
        <rect x="308" y="183" width="18" height="30" rx="2.5"/>
        <line x1="314" y1="209" x2="320" y2="209"/>
      </g>
      <text class="step-label" x="317" y="261">SELECT</text>
      <text class="step-label" x="317" y="274">PRODUCT</text>
      <text class="step-label" x="317" y="287">PROTECTION</text>
      <text class="step-label" x="317" y="300">PLAN</text>
    </g>

    <!-- step 3: register existing -->
    <g class="step step-existing">
      <circle class="node" cx="569" cy="246" r="56"/>
      <g class="icon">
        <rect x="557" y="227" width="20" height="36" rx="3"/>
        <line x1="564" y1="258" x2="570" y2="258"/>
      </g>
      <path class="icon-fill" d="M565 243 L579 243 L579 237 L590 246 L579 255 L579 249 L571 249 Z"/>
      <text class="step-label" x="569" y="322">REGISTER EXISTING</text>
      <text class="step-label" x="569" y="335">PRODUCTS</text>
    </g>

    <!-- step 4: register new -->
    <g class="step step-new">
      <circle class="node" cx="839" cy="147" r="40"/>
      <g class="icon">
        <rect x="826" y="127" width="26" height="40" rx="4"/>
        <line x1="826" y1="134" x2="852" y2="134"/>
        <line x1="826" y1="159" x2="852" y2="159"/>
        <circle cx="839" cy="163" r="1.3"/>
      </g>
      <text class="step-label" x="839" y="206">REGISTER NEW</text>
      <text class="step-label" x="839" y="219">PRODUCTS AS</text>
      <text class="step-label" x="839" y="232">PURCHASED</text>
    </g>

    <!-- step 5: sign up -->
    <g class="step step-signup">
      <circle class="node" cx="1103" cy="261" r="62"/>
      <g class="icon">
        <path d="M1094 271 Q1086 263 1086 254 A17 17 0 0 1 1120 254 Q1120 263 1112 271 Z"/>
        <line x1="1095" y1="276" x2="1111" y2="276"/>
        <line x1="1096" y1="281" x2="1110" y2="281"/>
        <line x1="1099" y1="286" x2="1107" y2="286"/>
        <path d="M1099 271 L1099 258 L1103 262 L1107 258 L1107 271"/>
        <line x1="1103" y1="226" x2="1103" y2="231"/>
        <line x1="1080" y1="236" x2="1084" y2="240"/>
        <line x1="1126" y1="236" x2="1122" y2="240"/>
        <line x1="1072" y1="254" x2="1077" y2="254"/>
        <line x1="1134" y1="254" x2="1129" y2="254"/>
        <line x1="1078" y1="268" x2="1082" y2="265"/>
        <line x1="1128" y1="268" x2="1124" y2="265"/>
      </g>
      <text class="step-label" x="1103" y="342">SIGN UP NOW</text>
    </g>
  </svg>
</section>
</body>
</html>
```